EV Charging Station Integrator needs a website for Brevok

We need a website to inform our customers and partners of what we do. At Brevok, we plan, design, and deploy EVcharging Solutions as a Service by leveraging a best-in-class multi-vendor and partner network with expertise to deliver EV Hardware, Software and Services as Turn-Key and Agnostic solutions.

The website should have 3 pages + contact (HOME, THE PROBLEM, THE SOLUTION) + Contact information. Please see PPT attached for suggested framework.

```html
<!DOCTYPE html>
<html lang="en">
<head>
<meta charset="utf-8">
<title>Brevok EV Charging</title>
<link href="https://fonts.googleapis.com/css2?family=Montserrat:wght@400;500;600;700;800&display=swap" rel="stylesheet">
<style>
:root{
  --navy:#2b2462;
  --navy-deep:#211b4f;
  --orange:#ff7a00;
  --amber:#ffb400;
  --yellow:#ffc20e;
  --ink:#1f1f1f;
  --grey:#6f6f6f;
  --peach:#fde3cf;
  --footer:#2b2b2b;
  --white:#ffffff;
}
*{box-sizing:border-box;margin:0;padding:0}
html,body{width:1200px;height:4508px;overflow:hidden}
body{font-family:"Montserrat",sans-serif;color:var(--ink);background:var(--white);position:relative}
.abs{position:absolute}

/* header */
.site-header{position:absolute;left:0;top:0;width:1200px;height:96px;background:var(--white);border-top:5px solid var(--navy-deep);z-index:3}
.brand-tab{position:absolute;left:112px;top:0;width:206px;height:132px;background:var(--white);clip-path:polygon(0 0,100% 0,100% 78%,92% 100%,8% 100%,0 78%);display:flex;align-items:center;justify-content:center;gap:10px}
.brand-tab .dot{width:16px;height:16px;background:var(--orange)}
.brand-tab .name{font-weight:700;font-size:24px;letter-spacing:4px;color:var(--navy)}
.main-nav{position:absolute;top:38px;left:463px;display:flex;align-items:center;font-size:13px;font-weight:700}
.main-nav a{color:var(--ink);text-decoration:none;margin-right:43px}
.btn-quote{border:2px solid var(--amber);padding:8px 16px;margin-right:16px!important}
.btn-contact{background:var(--orange);color:var(--white)!important;padding:10px 14px;margin:0!important}

/* hero */
.hero{position:absolute;left:0;top:96px;width:1200px;height:515px;background:var(--navy)}
.hero h1{position:absolute;left:112px;top:135px;font-size:56px;font-weight:800;line-height:64px;color:var(--white);letter-spacing:.5px;z-index:2;white-space:nowrap}
.hero h1 .hl-y{color:var(--amber)}
.hero h1 .hl-o{color:var(--orange)}
.btn-start{position:absolute;left:112px;top:416px;width:120px;height:33px;background:var(--orange);color:var(--white);font-size:12px;font-weight:700;display:flex;align-items:center;justify-content:center}
.hero-visual{position:absolute;left:640px;top:205px;width:470px;height:290px;border-radius:60px 60px 20px 20px;background:linear-gradient(160deg,#f4f6f8,#bfc6cf 70%,#8d96a3);z-index:1}

/* about */
.about-photo{left:112px;top:703px;width:385px;height:505px;border:6px solid var(--white);box-shadow:0 0 12px rgba(0,0,0,.12);background:linear-gradient(135deg,#c7d7ea,#4a7fc0 55%,#1d3f7a)}
.about-title{left:600px;top:700px;font-size:38px;font-weight:800}
.feature{left:600px;width:453px;background:var(--white);box-shadow:0 2px 10px rgba(0,0,0,.1);padding:20px 22px 0 98px}
.feature .ico{position:absolute;left:22px;top:20px;width:60px;height:60px;background:var(--yellow);border-radius:4px;display:flex;align-items:center;justify-content:center}
.feature h3{font-size:15px;font-weight:500;color:#333;margin-bottom:10px}
.feature p{font-size:11px;line-height:15px;color:var(--grey)}

/* how it works */
.how-bg{left:0;top:1290px;width:1200px;height:1210px}
.section-title{position:absolute;left:0;width:1200px;text-align:center;font-size:42px;font-weight:800}
.section-lede{position:absolute;left:175px;width:850px;text-align:center;font-size:15px;line-height:22px}
.how-title{top:1460px;color:var(--white)}
.how-lede{top:1530px;color:var(--white)}
.step{position:absolute;width:291px;height:290px;background:var(--white);text-align:center;padding-top:146px}
.step .num{position:absolute;left:18px;top:-48px;font-size:70px;font-weight:800;color:var(--amber);-webkit-text-stroke:2px var(--white)}
.circle-ico{position:absolute;left:50%;margin-left:-39px;top:40px;width:78px;height:78px;border-radius:50%;background:radial-gradient(circle at 50% 40%,var(--amber),var(--orange));box-shadow:0 0 0 5px #ffe7c2;display:flex;align-items:center;justify-content:center}
.step h3,.sol-card h3{font-size:21px;font-weight:700;margin-bottom:10px}
.step p,.sol-card p{font-size:13px;line-height:19px;color:var(--grey);padding:0 24px}

/* problem */
.problem-title{top:2555px}
.problem-lede{top:2627px;color:#555}
.slide-side{top:2745px;height:300px;background:linear-gradient(135deg,#0a1733,#1d4f9c 60%,#0d1e44)}
.slide-main{left:318px;top:2725px;width:563px;height:343px;border:4px solid var(--white);box-shadow:0 0 10px rgba(0,0,0,.15);background:linear-gradient(180deg,#3c4450,#6b6368 45%,#d98a3f 62%,#1b1d24)}
.slide-caption{left:385px;top:2955px;width:430px;height:110px;background:rgba(43,36,98,.9);color:var(--white);text-align:center;padding-top:20px}
.slide-caption h4{font-size:17px;font-weight:700;margin-bottom:10px}
.slide-caption p{font-size:9px;line-height:13px;padding:0 45px}
.arrow{top:2880px}

/* solution */
.solution-bg{left:0;top:3160px;width:1200px;height:645px}
.solution-title{top:3263px}
.solution-lede{top:3357px;color:#555}
.sol-card{position:absolute;top:3447px;width:291px;height:270px;background:var(--white);box-shadow:0 2px 10px rgba(0,0,0,.06);text-align:center;padding-top:150px}

/* contact */
.map{top:3805px;height:513px;background:linear-gradient(135deg,#e6eee0,#d5e6c9 50%,#eae7dc)}
.contact-panel{left:652px;top:3805px;width:436px;height:513px;background:var(--navy);color:var(--white);padding:58px 0 0 38px}
.contact-panel h2{font-size:40px;font-weight:700;margin-bottom:28px}
.contact-item{position:relative;padding-left:72px;height:78px}
.contact-item .pin{position:absolute;left:0;top:0;width:52px;height:52px;border-radius:50%;background:radial-gradient(circle at 50% 40%,var(--amber),var(--orange));display:flex;align-items:center;justify-content:center}
.contact-item h5{font-size:19px;font-weight:500;margin-bottom:8px;padding-top:2px}
.contact-item p{font-size:12px;line-height:16px}

/* footer */
.site-footer{position:absolute;left:0;top:4318px;width:1200px;height:190px;background:var(--footer);color:var(--white);text-align:center}
.foot-nav{position:absolute;top:80px;left:0;width:1200px;display:flex;justify-content:center;font-size:13px}
.foot-nav span{padding:0 48px}
.foot-nav i{font-style:normal}
.copyright{position:absolute;top:118px;width:1200px;font-size:13px}
.social{position:absolute;top:150px;left:548px;display:flex;gap:10px}
.social span{width:12px;height:12px;border-radius:50%;background:var(--white)}
</style>
</head>
<body>

<header class="site-header">
  <div class="brand-tab"><span class="dot"></span><span class="name">BREVOK</span></div>
  <nav class="main-nav">
    <a href="#">HOME</a>
    <a href="#">THE PROBLEM</a>
    <a href="#">THE SOLUTION</a>
    <a href="#" class="btn-quote">GET A QUOTE</a>
    <a href="#" class="btn-contact">CONTACT US</a>
  </nav>
</header>

<section class="hero">
  <h1>ENABLING <span class="hl-y">FAST</span><br>AND INTEGRATED<br><span class="hl-o">EV CHARGING</span><br>NETWORKS</h1>
  <div class="btn-start">GET STARTED</div>
  <div class="hero-visual" role="img" aria-label="White electric car plugged into a charging station"></div>
</section>

<div class="abs about-photo" role="img" aria-label="Electric car charging at a wall charger with glowing light trails"></div>
<h2 class="abs about-title">ABOUT US</h2>
<div class="abs feature" style="top:768px;height:112px">
  <div class="ico"><svg width="30" height="30" viewBox="0 0 30 30" fill="none" stroke="#222" stroke-width="2"><circle cx="15" cy="15" r="5"/><circle cx="15" cy="15" r="11" stroke-dasharray="4 3"/></svg></div>
  <h3>Best Of Breed Ecosystem</h3>
  <p>We plan, design, and deploy ev(1) charging solutions as a service by leveraging a best-in-class multi-vendor and partner network with expertise to deliver ev hardware, software and services as turn-key and agnostic solutions</p>
</div>
<div class="abs feature" style="top:922px;height:113px">
  <div class="ico"><svg width="30" height="30" viewBox="0 0 30 30" fill="none" stroke="#222" stroke-width="2"><circle cx="15" cy="15" r="11"/><path d="M17 7l-6 9h5l-3 7 7-10h-5z" fill="#222"/></svg></div>
  <h3>Scalability With Little To No Investment</h3>
  <p>We offer the ability to charge in minutes making for a scalable and nationwide application. The ev platform is delivered via consumption-based models allowing cities and enterprises to outsource the ev solution without prohibitive upfront investments</p>
</div>
<div class="abs feature" style="top:1077px;height:133px">
  <div class="ico"><svg width="30" height="30" viewBox="0 0 30 30" fill="#222"><path d="M15 5c4 4 4 9 0 13-4-4-4-9 0-13zM5 13c5 0 9 3 10 8-5 0-9-3-10-8zM25 13c-5 0-9 3-10 8 5 0 9-3 10-8z"/><rect x="14" y="20" width="2" height="6"/></svg></div>
  <h3>Sustainable Innovation</h3>
  <p>We enable a new, smart and high-power ev charging solution and consumer lifestyle powered by ai(2) with sustainability in mind. We incorporate solar and other co2 reducing technologies into our solution platform to augment power-limited grids</p>
</div>

<svg class="abs how-bg" viewBox="0 0 1200 1210" aria-hidden="true">
  <defs><linearGradient id="band" x1="0" x2="1"><stop offset="0" stop-color="#ff6a00"/><stop offset="1" stop-color="#ffb800"/></linearGradient></defs>
  <polygon points="0,135 860,0 1200,140 1200,170 0,160" fill="url(#band)"/>
  <polygon points="0,1060 1200,1060 1200,1120 250,1200 0,1080" fill="url(#band)"/>
  <polygon points="0,145 860,35 1200,150 1200,1100 250,1180 0,1070" fill="#2b2462"/>
</svg>
<h2 class="section-title how-title">HOW IT WORKS</h2>
<p class="section-lede how-lede">Lorem ipsum dolor sit amet, consectetur adipiscing elit, sed do eiusmod tempor incididunt ut labore et dolore magna aliqua. Quis ipsum suspendisse ultrices gravida.</p>

<div class="step" style="left:128px;top:1655px"><span class="num">1</span>
  <div class="circle-ico"><svg width="34" height="34" viewBox="0 0 34 34" fill="none" stroke="#fff" stroke-width="2.5"><circle cx="14" cy="14" r="8"/><path d="M20 20l8 8"/></svg></div>
  <h3>RESEARCH</h3><p>Access public funding allocated by municipalities. Engage partner network with signed municipal agreements to deploy public level 3</p></div>
<div class="step" style="left:455px;top:1655px"><span class="num">2</span>
  <div class="circle-ico"><svg width="34" height="34" viewBox="0 0 34 34" fill="none" stroke="#fff" stroke-width="2.5"><circle cx="17" cy="15" r="9"/><path d="M13 28h8"/></svg></div>
  <h3>CONCEPT</h3><p>Match private real state list with geographies where subsidies are available</p></div>
<div class="step" style="left:780px;top:1655px"><span class="num">3</span>
  <div class="circle-ico"><svg width="34" height="34" viewBox="0 0 34 34" fill="none" stroke="#fff" stroke-width="2.5"><path d="M8 26l4-12 12-6-6 12z"/><circle cx="17" cy="17" r="2"/></svg></div>
  <h3>DESIGN</h3><p>Identify optimal solution providers to deploy the EV charging platform</p></div>
<div class="step" style="left:291px;top:2018px"><span class="num">4</span>
  <div class="circle-ico"><svg width="34" height="34" viewBox="0 0 34 34" fill="none" stroke="#fff" stroke-width="2.5"><circle cx="17" cy="20" r="9"/><path d="M13 8h8l-2 3h-4z"/></svg></div>
  <h3>FUND</h3><p>Brevok and its investor partners provide the equity and debt capital to fuel the consumption-based model</p></div>
<div class="step" style="left:618px;top:2018px"><span class="num">5</span>
  <div class="circle-ico"><svg width="34" height="34" viewBox="0 0 34 34" fill="none" stroke="#fff" stroke-width="2.5"><path d="M10 24c2-10 8-16 16-16-1 8-6 14-16 16z"/><path d="M8 26l4-4"/></svg></div>
  <h3>DEPLOY / O&amp;M</h3><p>Brevok and its solution providers implement the EV charging platform, as well as on-going operations and maintenance of the network</p></div>

<h2 class="section-title problem-title">THE PROBLEM</h2>
<p class="section-lede problem-lede">Lorem ipsum dolor sit amet, consectetur adipiscing elit, sed do eiusmod tempor incididunt ut labore et dolore magna aliqua. Quis ipsum suspendisse ultrices gravida.</p>
<div class="abs slide-side" style="left:0;width:240px" role="img" aria-label="Charger plugged into an electric car with blue light trails"></div>
<div class="abs slide-side" style="left:955px;width:245px" role="img" aria-label="Glowing blue EV charging port close-up"></div>
<svg class="abs arrow" style="left:274px" width="18" height="30" viewBox="0 0 18 30" fill="none" stroke="#aaa" stroke-width="2"><path d="M15 3L3 15l12 12"/></svg>
<svg class="abs arrow" style="left:910px" width="18" height="30" viewBox="0 0 18 30" fill="none" stroke="#aaa" stroke-width="2"><path d="M3 3l12 12L3 27"/></svg>
<div class="abs slide-main" role="img" aria-label="Two cars facing a lone charging post at sunset"></div>
<div class="abs slide-caption">
  <h4>LIMITED &nbsp;CHARGING INFRASTRUCTURE</h4>
  <p>Current EV charging network is 70 miles apart. Primarily planned in cities and interstate highways, excluding rural, small cities and underserved areas.</p>
</div>

<svg class="abs solution-bg" viewBox="0 0 1200 645" aria-hidden="true">
  <defs><linearGradient id="peach" x1="0" y1="0" x2="0" y2="1"><stop offset="0" stop-color="#fde0c8"/><stop offset="1" stop-color="#fff8f2"/></linearGradient></defs>
  <polygon points="0,120 940,10 1200,120 1200,645 0,645" fill="url(#peach)"/>
</svg>
<h2 class="section-title solution-title">THE SOLUTION</h2>
<p class="section-lede solution-lede">End-to-end deployment and integration of ev charging solution as a service cities and enterprises outsource the ev infrastructure, billing and on-going maintenance</p>
<div class="sol-card" style="left:128px">
  <div class="circle-ico"><svg width="34" height="34" viewBox="0 0 34 34" fill="#fff"><rect x="7" y="10" width="9" height="18"/><rect x="18" y="6" width="9" height="22"/></svg></div>
  <h3>PUBLIC SECTOR</h3><p>Municipal areas &amp; ROWs (parking lots, sidewalks, airports and seaports, etc.)</p></div>
<div class="sol-card" style="left:455px">
  <div class="circle-ico"><svg width="34" height="34" viewBox="0 0 34 34" fill="#fff"><path d="M5 13L17 6l12 7z"/><rect x="8" y="15" width="3" height="10"/><rect x="15.5" y="15" width="3" height="10"/><rect x="23" y="15" width="3" height="10"/><rect x="5" y="26" width="24" height="3"/></svg></div>
  <h3>HYBRID</h3><p>High traffic private real estate (Retail, Banks, etc.)</p></div>
<div class="sol-card" style="left:780px">
  <div class="circle-ico"><svg width="34" height="34" viewBox="0 0 34 34" fill="#fff"><rect x="9" y="6" width="16" height="22"/><rect x="6" y="27" width="22" height="2"/></svg></div>
  <h3>PRIVATE</h3><p>Real Estate Investment Trust (REIT) (Hotels, apartments, malls, etc.)</p></div>

<div class="abs map" style="left:0;width:652px" role="img" aria-label="Road map of the service region"></div>
<div class="abs map" style="left:1088px;width:112px" role="img" aria-label="Road map continued"></div>
<div class="abs contact-panel">
  <h2>GET IN TOUCH</h2>
  <div class="contact-item"><span class="pin"><svg width="20" height="24" viewBox="0 0 20 24" fill="#fff"><path d="M10 0a8 8 0 018 8c0 6-8 16-8 16S2 14 2 8a8 8 0 018-8zm0 5a3 3 0 100 6 3 3 0 000-6z"/></svg></span><h5>Location</h5><p>418 Harlow Street</p></div>
  <div class="contact-item"><span class="pin"><svg width="22" height="22" viewBox="0 0 22 22" fill="#fff"><path d="M4 2l4 0 2 5-3 2a12 12 0 006 6l2-3 5 2v4a2 2 0 01-2 2C9 20 2 13 2 4a2 2 0 012-2z"/></svg></span><h5>Call Us</h5><p>555-014-2290</p></div>
  <div class="contact-item"><span class="pin"><svg width="22" height="16" viewBox="0 0 22 16" fill="none" stroke="#fff" stroke-width="2"><rect x="1" y="1" width="20" height="14"/><path d="M1 1l10 8 10-8"/></svg></span><h5>Email Us</h5><p>info@brevok.com</p></div>
  <div class="contact-item"><span class="pin"><svg width="22" height="22" viewBox="0 0 22 22" fill="none" stroke="#fff" stroke-width="2"><circle cx="11" cy="11" r="9"/><path d="M11 5v6l4 3"/></svg></span><h5>Working Hours</h5><p>Mon - Sat : 8.00 AM - 6.00 PM<br>Sun : Closed</p></div>
</div>

<footer class="site-footer">
  <div class="foot-nav"><span>HOME</span><i>|</i><span>ABOUT US</span><i>|</i><span>THE PROBLEM</span><i>|</i><span>THE SOLUTION</span><i>|</i><span>CONTACT US</span></div>
  <p class="copyright">COPYRIGHT © 2023 BREVOK EV CHARGING | ALL RIGHTS RESERVED</p>
  <div class="social"><span></span><span></span><span></span><span></span><span></span></div>
</footer>

</body>
</html>
```